Product Marketing Slick / Product Brief. 1 sheet now then an additional 2 plus more in the future.

We need to create 1 page product sheets that will be used for marketing purposes.
The products we are selling are network security and network compliance for PCI, HIPAA and GDPR.
We will essentially be doing all of the consulting to make their networks secure, then on a daily basis be scanning and validating that all of the government requirements are being met for compliance.
We dont want to make this too technical so its more of a page that will discuss in general terms what we do and why its important for them to have our services.
***Note There will be a total of Three Sheets, this project is for the first one and can be for any one of the products. HIPAA Compliance , PCI Compliance or GDPR Compliance.
We will contract with you to do the additional 2 pages and probably more if we select your design.
Target Market(s)
Medical, Hospitality
Industry/Entity Type
Medical
Colors
Designer to choose colors to be used in the design.

```html
<!DOCTYPE html>
<html lang="en">
<head>
<meta charset="utf-8">
<title>Veridane Compliance Product Sheet – Samples</title>
<link rel="stylesheet" href="https://fonts.googleapis.com/css2?family=Montserrat:wght@300;400;500;600;700;800&display=swap">
<style>
  :root {
    --board: #484848;
    --paper: #ffffff;
    --navy: #1f1d5c;
    --green: #8cc63f;
    --green-light: #9fd06a;
    --green-dark: #7cb944;
    --grey-swoosh: #d9d9d9;
    --photo-light: #f4f6f8;
    --photo-mid: #cfd6de;
    --body-text: #222222;
    --label: #f2f2f2;
  }
  * { box-sizing: border-box; margin: 0; padding: 0; }
  html, body { width: 1200px; height: 888px; overflow: hidden; background: var(--board); }
  body { position: relative; font-family: "Montserrat", sans-serif; }

  .sheet {
    position: absolute; top: 72px; width: 538px; height: 692px;
    background: var(--paper); overflow: hidden;
    box-shadow: 0 10px 18px rgba(0,0,0,.35);
  }
  .sheet--curve { left: 48px; }
  .sheet--angle { left: 626px; width: 536px; }

  .brand { position: absolute; display: flex; align-items: center; gap: 10px; }
  .brand__mark { flex: none; background: var(--green-light); }
  .brand__name { color: var(--navy); font-weight: 700; white-space: nowrap; line-height: 1; }

  .headline div { position: absolute; left: 22px; line-height: 1; white-space: nowrap; }
  .headline .smart { color: var(--navy); font-weight: 300; }
  .headline .simple { color: var(--green); font-weight: 300; }
  .headline .safe { color: var(--green); font-weight: 800; }
  .headline .secure { color: var(--navy); font-weight: 800; letter-spacing: -1px; }

  .photo { position: absolute; }

  .standards {
    position: absolute; left: 358px; top: 344px; width: 163px;
    border-radius: 0 0 12px 12px; overflow: hidden;
  }
  .standards div {
    height: 38px; line-height: 38px; text-align: center;
    color: #fff; font-weight: 800; font-size: 29px;
  }
  .standards .row-light { background: var(--green-light); }
  .standards .row-dark { background: var(--green-dark); }

  .tagline-block { position: absolute; white-space: nowrap; line-height: 1; }
  .tagline-block .lead { color: var(--navy); font-weight: 600; }
  .tagline-block .follow { font-weight: 800; }
  .rule { position: absolute; height: 3px; background: var(--green); }

  .body-copy {
    position: absolute; left: 23px; width: 493px;
    font-size: 10px; line-height: 12.8px; color: var(--body-text);
    text-align: justify;
  }
  .body-copy p { margin-bottom: 4.5px; }

  .contact-bar {
    position: absolute; left: 0; right: 0; top: 650px; height: 38px;
    background: var(--navy); color: #fff;
  }
  .contact-bar .address { position: absolute; left: 18px; top: 12px; font-size: 8.5px; font-weight: 700; display: flex; align-items: center; gap: 6px; }
  .contact-bar .phone { position: absolute; left: 190px; top: 6px; font-size: 21px; font-weight: 800; display: flex; align-items: center; gap: 7px; }
  .contact-bar .web {
    position: absolute; left: 370px; right: 0; top: 5px; height: 28px;
    background: #fff; border-radius: 14px 0 0 14px; color: var(--navy);
    font-size: 11px; font-weight: 800; display: flex; align-items: center; gap: 7px; padding-left: 6px;
  }
  .icon { flex: none; }

  .sample-label {
    position: absolute; top: 820px; width: 300px; text-align: center;
    color: var(--label); font-size: 34px; font-weight: 300; letter-spacing: 1px;
  }
</style>
</head>
<body>

<section class="sheet sheet--curve">
  <svg class="photo" width="538" height="470" viewBox="0 0 538 470" role="img" aria-label="Photo of a doctor in a white coat giving a thumbs up">
    <defs>
      <linearGradient id="photoFadeA" x1="0" y1="0" x2="1" y2="0">
        <stop offset="0" stop-color="#ffffff"/>
        <stop offset=".45" stop-color="#f4f6f8"/>
        <stop offset="1" stop-color="#cfd6de"/>
      </linearGradient>
    </defs>
    <path d="M0 0 H538 V250 Q330 420 0 265 Z" fill="url(#photoFadeA)"/>
    <path d="M0 262 Q200 380 420 362 Q300 395 0 275 Z" fill="var(--grey-swoosh)"/>
    <path d="M20 275 Q250 390 538 248 L538 272 Q500 320 521 344 L358 344 Q200 370 20 275 Z" fill="var(--green)"/>
  </svg>

  <div class="brand" style="left:24px;top:38px;">
    <span class="brand__mark" style="width:22px;height:22px;"></span>
    <span class="brand__name" style="font-size:20px;">Veridane</span>
  </div>

  <div class="headline">
    <div class="smart" style="top:90px;font-size:54px;">SMART</div>
    <div class="simple" style="top:140px;font-size:40px;">SIMPLE</div>
    <div class="safe" style="top:172px;font-size:44px;">SAFE</div>
    <div class="secure" style="top:212px;font-size:45px;">SECURE</div>
  </div>

  <div class="standards">
    <div class="row-light">HIPAA</div>
    <div class="row-dark">PCI</div>
    <div class="row-light">GDPR</div>
  </div>

  <div class="tagline-block" style="left:22px;top:400px;">
    <div class="lead" style="font-size:27px;">WE WORRY, SO</div>
    <div class="follow" style="font-size:25.5px;color:var(--green);margin-top:3px;">YOU DON'T HAVE TO</div>
  </div>
  <span class="rule" style="left:22px;top:463px;width:62px;"></span>

  <div class="body-copy" style="top:478px;">
    <p>Veridane has been securing networks for over twenty years and was one of the first managed security companies in the country. Thousands of satisfied and secured customers can't be wrong. There's a reason for our longevity and we want to pass that on to you. As the times and threats have changed so have we, adapting and overcoming each new menace that arises, staying at the forefront of technology so we can keep you safe.</p>
    <p>Compliance is a key component not only to keeping your safe and secure but also to ensure your organization is up to speed on all new government regulations and requirements.</p>
    <p>Do you really want to know all the complexities of HIPAA and PCI compliance? Yes? We'll teach you everything you need to know.</p>
    <p>No? We'll handle everything from start to finish and manage and maintain it so you never have to think or worry about it again.</p>
  </div>

  <footer class="contact-bar">
    <span class="address">
      <svg class="icon" width="12" height="12" viewBox="0 0 12 12"><circle cx="6" cy="6" r="6" fill="var(--green)"/><path d="M6 2.5a2.3 2.3 0 0 0-2.3 2.3C3.7 6.5 6 9.5 6 9.5s2.3-3 2.3-4.7A2.3 2.3 0 0 0 6 2.5z" fill="#fff"/><circle cx="6" cy="4.8" r=".9" fill="var(--green)"/></svg>
      Company Address Goes Here
    </span>
    <span class="phone">
      <svg class="icon" width="14" height="14" viewBox="0 0 14 14"><circle cx="7" cy="7" r="7" fill="var(--green)"/><path d="M4.3 3.6l1.3-.2.7 1.7-.8.6a5 5 0 0 0 2.8 2.8l.6-.8 1.7.7-.2 1.3c-3.3.3-6.4-2.8-6.1-6.1z" fill="#fff"/></svg>
      0123 456 789
    </span>
    <span class="web">
      <svg class="icon" width="14" height="14" viewBox="0 0 14 14" fill="none" stroke="var(--green)" stroke-width="1"><circle cx="7" cy="7" r="6"/><ellipse cx="7" cy="7" rx="2.6" ry="6"/><path d="M1 7h12M2 4h10M2 10h10"/></svg>
      www.yourwebsite.com
    </span>
  </footer>
</section>

<section class="sheet sheet--angle">
  <div class="brand" style="left:0;right:0;top:36px;justify-content:center;">
    <span class="brand__mark" style="width:26px;height:26px;"></span>
    <span class="brand__name" style="font-size:24px;">Veridane</span>
  </div>

  <svg class="photo" style="left:240px;top:90px;" width="296" height="232" viewBox="0 0 296 232" role="img" aria-label="Photo of a doctor in a white coat giving a thumbs up">
    <defs>
      <linearGradient id="photoFadeB" x1="0" y1="0" x2="1" y2="0">
        <stop offset="0" stop-color="#2b3440"/>
        <stop offset=".3" stop-color="#cfd6de"/>
        <stop offset="1" stop-color="#f4f6f8"/>
      </linearGradient>
    </defs>
    <path d="M60 0 H296 V232 H0 Z" fill="url(#photoFadeB)"/>
  </svg>

  <div class="headline">
    <div class="smart" style="top:108px;font-size:58px;">SMART</div>
    <div class="simple" style="top:160px;font-size:45px;">SIMPLE</div>
    <div class="safe" style="top:198px;font-size:50px;">SAFE</div>
    <div class="secure" style="top:242px;font-size:51px;">SECURE</div>
  </div>

  <div class="tagline-block" style="left:0;right:0;top:342px;text-align:center;">
    <div class="lead" style="font-size:27px;">WE WORRY, SO</div>
    <div class="follow" style="font-size:27px;color:var(--navy);margin-top:2px;">YOU DON'T HAVE TO</div>
    <div class="follow" style="font-size:22px;color:var(--green);margin-top:8px;">HIPAA • PCI • GDPR</div>
  </div>
  <span class="rule" style="left:234px;top:437px;width:69px;"></span>

  <div class="body-copy" style="top:464px;">
    <p>Veridane has been securing networks for over twenty years and was one of the first managed security companies in the country. Thousands of satisfied and secured customers can't be wrong. There's a reason for our longevity and we want to pass that on to you. As the times and threats have changed so have we, adapting and overcoming each new menace that arises, staying at the forefront of technology so we can keep you safe.</p>
    <p>Compliance is a key component not only to keeping your safe and secure but also to ensure your organization is up to speed on all new government regulations and requirements.</p>
    <p>Do you really want to know all the complexities of HIPAA and PCI compliance? Yes? We'll teach you everything you need to know.</p>
    <p>No? We'll handle everything from start to finish and manage and maintain it so you never have to think or worry about it again.</p>
  </div>

  <footer class="contact-bar">
    <span class="address">
      <svg class="icon" width="12" height="12" viewBox="0 0 12 12"><circle cx="6" cy="6" r="6" fill="var(--green)"/><path d="M6 2.5a2.3 2.3 0 0 0-2.3 2.3C3.7 6.5 6 9.5 6 9.5s2.3-3 2.3-4.7A2.3 2.3 0 0 0 6 2.5z" fill="#fff"/><circle cx="6" cy="4.8" r=".9" fill="var(--green)"/></svg>
      Company Address Goes Here
    </span>
    <span class="phone">
      <svg class="icon" width="14" height="14" viewBox="0 0 14 14"><circle cx="7" cy="7" r="7" fill="var(--green)"/><path d="M4.3 3.6l1.3-.2.7 1.7-.8.6a5 5 0 0 0 2.8 2.8l.6-.8 1.7.7-.2 1.3c-3.3.3-6.4-2.8-6.1-6.1z" fill="#fff"/></svg>
      0123 456 789
    </span>
    <span class="web">
      <svg class="icon" width="14" height="14" viewBox="0 0 14 14" fill="none" stroke="var(--green)" stroke-width="1"><circle cx="7" cy="7" r="6"/><ellipse cx="7" cy="7" rx="2.6" ry="6"/><path d="M1 7h12M2 4h10M2 10h10"/></svg>
      www.yourwebsite.com
    </span>
  </footer>
</section>

<div class="sample-label" style="left:164px;">SAMPLE 1</div>
<div class="sample-label" style="left:724px;">SAMPLE 2</div>

</body>
</html>
```